Tobins Jewelry needs a Magazine AD

We need a full page magazine advertisement that can drive customers to our store for the holiday season. The ad needs to incorporate the three jewelry pictures attached. The ad will be featured on the back cover of a local magazine that reaches every resident in our city. We would like a clean style AD. We would not like it to be cluttered.

The dimensions of the project are as follows for printing
8.5" wide
11" tall
Bleed full and spreads
add an additional 1/4" to each outside edge

The project must have the three pictures of jewelry in the AD, our logo, It also needs to have our address, phone number, and instagram address

4876 Larkspur Blvd.
La Verne, Ca
(909)418-2265
Instagram.com/tobinsjewelrystudio
www.TobinsJewelryStudio.example

Target Market(s)

Women ages 25-55

Industry/Entity Type

Jewelry Store

Colors
85cae6
32a6d6

Requirements
Must have
• The dimensions of the project are as follows for printing
• 8.5" wide
• 11" tall
• Bleed full and spreads
• add an additional 1/4" to each outside edge
• The project must have the three pictures of jewelry in the AD, our logo, It also needs to have our address, phone number, and instagram address
• 4876 Larkspur Blvd.
• La Verne, Ca
• (909)418-2265
• Instagram.com/tobinsjewelrystudio
• www.TobinsJewelryStudio.example
Nice to have
• It would be nice to have
• "Moving to downtown La Verne in 2017"
Should not have
• My project must not have any cheesy coupon looks or any stock photos.

```html
<!DOCTYPE html>
<html lang="en">
<head>
<meta charset="utf-8">
<title>Tobin's Jewelry Studio – Magazine Ad</title>
<link href="https://fonts.googleapis.com/css2?family=Questrial&family=Montserrat:wght@600;700&display=swap" rel="stylesheet">
<style>
  :root {
    --page-bg: #e9ecef;
    --header-top: #0866b8;
    --header-bottom: #2092d8;
    --body-edge: #2ba3dc;
    --body-mid: #8cc9e8;
    --glow: #f4f9fd;
    --diamond-light: #bfe4f3;
    --diamond-edge: #7fc6e8;
    --award-top: #1a9bd8;
    --award-bottom: #1284c8;
    --footer: #16a4dc;
    --logo-dot: #bfe6ef;
    --text-light: #ffffff;
    --rose-gold-light: #e9c3a6;
    --rose-gold: #d59a78;
    --gold-light: #e6d39a;
    --gold: #c8aa5c;
    --turquoise: #5cc3e4;
  }
  * { margin: 0; padding: 0; box-sizing: border-box; }
  html, body { width: 1200px; height: 1200px; overflow: hidden; background: var(--page-bg); }

  .ad {
    position: absolute;
    left: 157px; top: 30px;
    width: 830px; height: 1067px;
    transform: scale(1.068);
    transform-origin: top left;
    overflow: hidden;
    font-family: "Questrial", sans-serif;
    color: var(--text-light);
    background:
      radial-gradient(ellipse 330px 380px at 415px 640px, var(--glow) 0%, var(--body-mid) 45%, var(--body-edge) 100%);
  }

  .ad__header {
    position: absolute; left: 0; top: 0; width: 830px; height: 172px;
    background: linear-gradient(var(--header-top), var(--header-bottom));
    border-bottom: 1px solid rgba(255,255,255,0.55);
  }
  .brand {
    position: absolute; left: 150px; top: 78px; width: 530px; height: 36px;
    display: flex; align-items: center; justify-content: center; gap: 14px;
  }
  .brand__rule { flex: 1; height: 3px; background: #3a2015; }
  .brand__dot { width: 30px; height: 30px; border-radius: 50%; background: var(--logo-dot); }
  .brand__name {
    font-family: "Montserrat", sans-serif; font-weight: 700; font-size: 24px;
    letter-spacing: 0.5px; color: var(--text-light); white-space: nowrap;
  }

  .headline {
    position: absolute; left: 0; top: 214px; width: 830px;
    text-align: center; font-weight: 400; font-size: 28px; line-height: 37px;
    text-transform: uppercase; letter-spacing: 0.3px;
  }

  .shapes { position: absolute; left: 0; top: 0; }

  .product {
    position: absolute;
    border-radius: 10px;
    border: 1px solid rgba(255,255,255,0.6);
  }
  .product--necklace {
    left: 380px; top: 338px; width: 70px; height: 354px;
    background: linear-gradient(var(--rose-gold-light), var(--rose-gold));
  }
  .product--ring {
    left: 128px; top: 642px; width: 165px; height: 140px;
    background: linear-gradient(var(--gold-light), var(--gold));
  }
  .product--earrings {
    left: 490px; top: 670px; width: 262px; height: 110px;
    background: linear-gradient(90deg, var(--turquoise), var(--rose-gold-light));
  }

  .award {
    position: absolute; left: 215px; top: 834px; width: 400px;
    text-align: center; font-size: 19px; line-height: 24px;
  }
  .award__name { font-family: "Montserrat", sans-serif; font-weight: 700; font-size: 18px; }

  .ad__footer {
    position: absolute; left: 0; top: 968px; width: 830px; height: 99px;
    background: var(--footer);
    text-align: center; font-size: 15px; line-height: 19px; padding-top: 10px;
  }
  .ad__footer .phone { font-family: "Montserrat", sans-serif; font-weight: 700; font-size: 14px; }
</style>
</head>
<body>
  <main class="ad">
    <header class="ad__header">
      <div class="brand">
        <span class="brand__rule"></span>
        <span class="brand__dot"></span>
        <span class="brand__name">tobin's jewelry studio</span>
        <span class="brand__rule"></span>
      </div>
    </header>

    <h1 class="headline">Specializes in custom design,<br>bridal, and designer jewelry in platinum,<br>gold and silver.</h1>

    <svg class="shapes" width="830" height="1067" viewBox="0 0 830 1067">
      <defs>
        <linearGradient id="diamondFill" x1="0" y1="0" x2="0" y2="1">
          <stop offset="0" stop-color="#bfe4f3" stop-opacity="0.85"/>
          <stop offset="1" stop-color="#7fc6e8" stop-opacity="0.9"/>
        </linearGradient>
        <linearGradient id="awardFill" x1="0" y1="0" x2="0" y2="1">
          <stop offset="0" stop-color="#1a9bd8"/>
          <stop offset="1" stop-color="#1284c8"/>
        </linearGradient>
      </defs>
      <polygon class="diamond diamond--left" points="210,510 410,710 210,910 10,710" fill="url(#diamondFill)"/>
      <polygon class="diamond diamond--right" points="620,510 820,710 620,910 420,710" fill="url(#diamondFill)"/>
      <polygon class="diamond diamond--award" points="415,717 615,917 564,968 266,968 215,917" fill="url(#awardFill)"/>
    </svg>

    <div class="product product--necklace" role="img" aria-label="Rose gold pendant necklace with a double triangle drop set with diamonds"></div>
    <div class="product product--ring" role="img" aria-label="Yellow gold bypass ring with two pavé diamond leaf shapes"></div>
    <div class="product product--earrings" role="img" aria-label="Rose gold stud earrings with round turquoise stones and diamond halos, front and side view"></div>

    <p class="award">
      <span class="award__name">Tobin's Jewelry Studio</span><br>
      was honored with<br>
      the Readers Choice<br>
      Award in 2012 and 2014
    </p>

    <footer class="ad__footer">
      4876 Larkspur Blvd. La Verne, Ca<br>
      <span class="phone">(909)418-2265</span><br>
      Instagram.com/tobinsjewelrystudio &nbsp;|&nbsp; www.TobinsJewelryStudio.example
    </footer>
  </main>
</body>
</html>
```